Business Card Design

Company name is: Ridgeline Lifeguard Training, LLC. We teach CPR/AED, First Aid, Bloodborne Pathogens and other health and safety classes. Looking for an eye-catching, progressive, cutting edge design.

Industry/Entity Type

Health

Contact Information for Business Card

Tom Wexford (555.218.4073)
June Pellicott (555.862.1940)
email is info@ridgelinetraininghq.com
website is www.RidgelineTrainingHQ.com

```html
<!DOCTYPE html>
<html lang="en">
<head>
<meta charset="utf-8">
<title>Ridgeline Lifeguard Training, LLC – Business Card</title>
<link rel="stylesheet" href="https://fonts.googleapis.com/css2?family=Open+Sans:wght@400;500&display=swap">
<style>
  :root {
    --brand-blue: #1a8fd0;
    --brand-red: #e31e2d;
    --ink: #111111;
    --rule: #e9a2a7;
    --paper: #ffffff;
  }
  html, body {
    margin: 0;
    padding: 0;
    overflow: hidden;
    background: var(--paper);
  }
  .card {
    position: relative;
    width: 1200px;
    height: 704px;
    background: var(--paper);
    font-family: "Open Sans", Arial, sans-serif;
    overflow: hidden;
  }
  .brand-mark {
    position: absolute;
    left: 520px;
    top: 58px;
    width: 160px;
    height: 160px;
  }
  .company-block {
    position: absolute;
    left: 0;
    right: 0;
    top: 262px;
    display: flex;
    justify-content: center;
  }
  .company-name {
    margin: 0;
    padding: 10px 22px 12px;
    border-top: 1.5px solid var(--rule);
    border-bottom: 1.5px solid var(--rule);
    color: var(--brand-blue);
    font-weight: 400;
    font-size: 42px;
    line-height: 44px;
    letter-spacing: 0.5px;
    white-space: nowrap;
  }
  .services {
    position: absolute;
    left: 0;
    right: 0;
    top: 377px;
    margin: 0;
    text-align: center;
    color: var(--brand-red);
    font-weight: 500;
    font-size: 29px;
    letter-spacing: 0.3px;
  }
  .contacts {
    position: absolute;
    left: 0;
    right: 0;
    top: 465px;
    margin: 0;
    padding: 0;
    list-style: none;
    text-align: center;
    color: var(--ink);
    font-size: 30px;
  }
  .contacts li {
    height: 60px;
    line-height: 42px;
  }
  .phone {
    color: var(--brand-blue);
  }
  .online {
    position: absolute;
    left: 0;
    right: 0;
    top: 612px;
    margin: 0;
    text-align: center;
    color: var(--ink);
    font-size: 30px;
  }
  .online .label {
    color: var(--brand-red);
  }
  .online .divider {
    color: var(--brand-blue);
    padding: 0 6px;
  }
</style>
</head>
<body>
  <div class="card">
    <svg class="brand-mark" viewBox="0 0 160 160" aria-hidden="true">
      <circle cx="80" cy="80" r="78" fill="var(--brand-red)"/>
    </svg>

    <div class="company-block">
      <h1 class="company-name">RIDGELINE LIFEGUARD TRAINING, LLC.</h1>
    </div>

    <p class="services">CPR/AED, FIRST AID &amp; BLOODBORNE PATHEGON TRAINING</p>

    <ul class="contacts">
      <li>Tom Wexford - <span class="phone">555.218.4073</span></li>
      <li>June Pellicott - <span class="phone">555.862.1940</span></li>
    </ul>

    <p class="online">
      <span class="label">Email:</span> info@ridgelinetraininghq.com
      <span class="divider">|</span>
      <span class="label">Web:</span> www.ridgelinetraininghq.com
    </p>
  </div>
</body>
</html>
```